New Website - vostimo.net

This is what we looking for - http://www.craftlane-example.com/design/583017
Updates

hello, im back and i want some good designs for my website.. i need really creative ideas. this is for a cellphone provider company. Vostimo mobile please provide me a good ideas and i will go with u also to program the website

Font styles to use
Sans Serif

```html
<!DOCTYPE html>
<html lang="en">
<head>
<meta charset="utf-8">
<title>Vostimo Communications</title>
<link href="https://fonts.googleapis.com/css2?family=Arimo:wght@400;700&display=swap" rel="stylesheet">
<style>
:root{
  --bg-top:#2e2e2e;
  --bg-bottom:#5fa9e2;
  --page:#ffffff;
  --soft:#f7f7f7;
  --ink:#333333;
  --muted:#777777;
  --line:#d6d6d6;
  --blue:#1a8ad4;
  --cyan:#00b0e6;
  --green:#1f8a5c;
  --dark:#2b2b2b;
}
*{box-sizing:border-box;margin:0;padding:0}
html,body{width:1200px;height:1182px;overflow:hidden}
body{font-family:"Arimo",Arial,sans-serif;color:var(--ink);
  background:linear-gradient(180deg,var(--bg-top) 0,#3d4a58 330px,#4f8fc8 620px,var(--bg-bottom) 1182px);position:relative}
.abs{position:absolute}
.page{left:93px;top:31px;width:1007px;height:1045px;background:var(--page)}
.brand{left:74px;top:60px;width:301px;height:80px;background:#000;display:flex;align-items:center;padding-left:30px;gap:14px;color:#fff}
.brand-dot{width:34px;height:34px;border-radius:50%;background:#2fa7e6}
.brand-name{font-size:38px;line-height:1;font-weight:400}
.brand-sub{font-size:12px;letter-spacing:3.5px;margin-top:3px}
.brand-fold{left:74px;top:140px}
.field{top:63px;height:28px;border:1px solid var(--line);border-radius:3px;font-size:10px;color:#999;padding:8px 7px;background:#fff}
.field.btn{text-align:center;color:#888}
.nav{top:122px;font-size:14px;color:#555;letter-spacing:.2px}
.nav.on{color:var(--blue)}
.nav-bar{left:484px;top:143px;width:51px;height:3px;background:#888}
.slider{left:116px;top:175px;width:960px;height:326px;background:#eee;border:2px solid #e6e6e6}
.tab{top:0;width:65px;height:322px;background:linear-gradient(90deg,#f0f0f0,#fff 60%,#e9e9e9);border-right:1px solid #ddd;box-shadow:2px 0 4px rgba(0,0,0,.08)}
.tab span{position:absolute;left:50%;bottom:20px;transform-origin:0 0;transform:rotate(-90deg) translateY(-50%);white-space:nowrap;font-size:18px;font-weight:700;color:#444}
.slide{left:262px;top:0;width:635px;height:322px;background:linear-gradient(180deg,#fff,#ececec)}
.slide h1{position:absolute;left:21px;top:30px;font-size:27px;color:var(--green)}
.slide p{position:absolute;left:21px;top:87px;width:300px;font-size:20px;line-height:37px;color:#666}
.photo{left:310px;top:0;width:325px;height:322px;background:linear-gradient(180deg,#e9eef3 0,#dfe5ea 100%)}
.col{top:536px;width:320px}
.col h2{font-size:20px;font-weight:400;color:var(--blue)}
.col h3{font-size:12px;font-weight:400;color:#444;margin-top:4px}
.col ul{list-style:none;margin-top:22px}
.col li{font-size:13.5px;color:#777;height:29px;display:flex;align-items:center;gap:9px;white-space:nowrap}
.col .btn{margin-top:12px;display:inline-block;height:32px;padding:0 12px;line-height:30px;font-size:12px;color:#444;background:linear-gradient(#f4f4f4,#e2e2e2);border:1px solid #ccc;border-radius:3px}
.lower{left:93px;top:768px;width:1007px;height:308px;background:var(--soft)}
.video{left:112px;top:790px;width:467px;height:262px;border:3px solid #e4e4e4;background:linear-gradient(135deg,#8a7a5a,#c9ae80 45%,#6e5d44)}
.play{left:300px;top:872px;width:76px;height:76px;border-radius:50%;background:rgba(255,255,255,.35);border:3px solid rgba(255,255,255,.85)}
.ctrl{left:118px;top:1027px;width:455px;height:19px;background:#d8d8d8;border-radius:2px}
.offer{left:598px;top:808px;width:182px}
.offer h4{font-size:19px;font-weight:400;color:#333}
.offer p{font-size:12.5px;line-height:20px;color:#888;margin-top:12px}
.offer ul{list-style:none;margin-top:6px}
.offer li{font-size:13px;font-weight:700;color:#666;height:24.5px;display:flex;align-items:center;gap:7px}
.search{left:787px;top:801px;width:332px;height:51px;background:var(--cyan);display:flex;align-items:center;padding-left:13px;gap:8px;color:#fff;font-weight:700;font-size:15px}
.search-box{width:212px;height:33px;background:#fff;border-radius:3px;font-size:12px;font-weight:400;color:#aaa;padding:10px;position:relative}
.fold{left:1100px;top:852px}
.touch{left:811px;top:873px;width:280px}
.touch h4{font-size:19px;font-weight:400;color:#333;margin-bottom:18px}
.touch dl{display:grid;grid-template-columns:73px 1fr;font-size:12.5px;line-height:20.5px;color:#777}
.touch dt{font-weight:700;color:#555}
.touch a{color:var(--blue);font-weight:700;text-decoration:none}
.footer{left:94px;top:1091px;width:1006px;height:53px;background:var(--dark);color:#bbb;font-size:11px;padding:20px 22px}
</style>
</head>
<body>
<div class="abs page"></div>

<div class="abs brand"><div class="brand-dot"></div><div><div class="brand-name">Vostimo</div><div class="brand-sub">COMMUNICATIONS</div></div></div>
<svg class="abs brand-fold" width="18" height="18"><polygon points="0,0 18,0 18,18" fill="#777"/></svg>

<div class="abs field" style="left:782px;width:107px">USER ID</div>
<div class="abs field" style="left:898px;width:107px">•••••••••</div>
<div class="abs field btn" style="left:1013px;width:56px">LOGIN</div>

<div class="abs nav on" style="left:490px">HOME</div>
<div class="abs nav" style="left:563px">ABOUT US</div>
<div class="abs nav" style="left:665px">SERVICES</div>
<div class="abs nav" style="left:767px">PRICE SHEET</div>
<div class="abs nav" style="left:889px">SUPPORT</div>
<div class="abs nav" style="left:987px">CONTACT US</div>
<div class="abs nav-bar"></div>

<div class="abs slider">
  <div class="abs tab" style="left:0"><span>Technical Support</span></div>
  <div class="abs tab" style="left:65px"><span>Cutting-edge Performance</span></div>
  <div class="abs tab" style="left:130px"><span>Enterprise Design</span></div>
  <div class="abs tab" style="left:195px"><span>Total Control</span></div>
  <div class="abs slide">
    <div class="abs photo" role="img" aria-label="Hands raised together holding up a globe"></div>
    <h1>Total Control</h1>
    <p>Our Hosted PBX system is designed for easy control over your entire communication system.</p>
  </div>
  <div class="abs tab" style="left:897px"><span>Why Hosted PBX?</span></div>
</div>

<svg width="0" height="0" style="position:absolute"><defs><symbol id="tick" viewBox="0 0 16 14"><path d="M2 7 L6 11 L14 2" fill="none" stroke="#bbb" stroke-width="2.4" stroke-linecap="round"/></symbol></defs></svg>

<div class="abs col" style="left:123px">
  <h2>AFFORDABLE</h2><h3>START SAVING TODAY!</h3>
  <ul>
    <li><svg width="16" height="14"><use href="#tick"/></svg>Unlimited local and long distance calling</li>
    <li><svg width="16" height="14"><use href="#tick"/></svg>5 nation unlimited international</li>
    <li><svg width="16" height="14"><use href="#tick"/></svg>No set-up equipment fees, or hidden charges</li>
    <li><svg width="16" height="14"><use href="#tick"/></svg>No contracts or commitments</li>
  </ul>
  <span class="btn">Compare Rates &amp; Plans »</span>
</div>
<div class="abs col" style="left:453px">
  <h2>POWERFUL</h2><h3>INCREDIBLE FEATURES, STANDARD</h3>
  <ul>
    <li><svg width="16" height="14"><use href="#tick"/></svg>Seamless integration with Mailbridge</li>
    <li><svg width="16" height="14"><use href="#tick"/></svg>Get calls and voicemail anywhere</li>
    <li><svg width="16" height="14"><use href="#tick"/></svg>100% hurricane proof</li>
    <li><svg width="16" height="14"><use href="#tick"/></svg>Featuring the power of Callweave!</li>
  </ul>
  <span class="btn">Click for more Features »</span>
</div>
<div class="abs col" style="left:779px">
  <h2>FLEXIBLE</h2><h3>SERVICE ON YOUR OWN TERMS</h3>
  <ul>
    <li><svg width="16" height="14"><use href="#tick"/></svg>Unlimited local and long distance calling</li>
    <li><svg width="16" height="14"><use href="#tick"/></svg>5 nation unlimited international</li>
    <li><svg width="16" height="14"><use href="#tick"/></svg>No set-up equipment fees, or hidden charges</li>
    <li><svg width="16" height="14"><use href="#tick"/></svg>No contracts or commitments</li>
  </ul>
  <span class="btn">Learn How it Works »</span>
</div>

<div class="abs lower"></div>
<div class="abs video" role="img" aria-label="Video still of a presenter speaking in a warm-lit office"></div>
<div class="abs play"></div>
<svg class="abs" style="left:326px;top:893px" width="30" height="36"><path d="M5 3 L26 18 L5 33 Z" fill="none" stroke="#444" stroke-width="3" stroke-linejoin="round"/></svg>
<div class="abs ctrl"></div>
<div class="abs" style="left:144px;top:1032px;width:400px;height:9px;background:#f2f2f2;border:1px solid #bbb"></div>

<div class="abs offer">
  <h4>What we offer?</h4>
  <p>Vostimo brings unsurpassed quality, reliability and service to your personal and business telecommunication network.</p>
  <ul>
    <li><svg width="16" height="14"><use href="#tick"/></svg>VoIP Services</li>
    <li><svg width="16" height="14"><use href="#tick"/></svg>Hosted PBX</li>
    <li><svg width="16" height="14"><use href="#tick"/></svg>Voicemail Service</li>
    <li><svg width="16" height="14"><use href="#tick"/></svg>Virtual Fax</li>
    <li><svg width="16" height="14"><use href="#tick"/></svg>Vostimo IVR</li>
  </ul>
</div>

<div class="abs search">SEARCH:
  <div class="search-box">Search site
    <svg style="position:absolute;right:10px;top:7px" width="20" height="20"><circle cx="8" cy="8" r="6" fill="#eef6fb" stroke="#888" stroke-width="2"/><path d="M12.5 12.5 L18 18" stroke="#666" stroke-width="3" stroke-linecap="round"/></svg>
  </div>
</div>
<svg class="abs fold" width="19" height="19"><polygon points="0,0 19,0 0,19" fill="#111"/></svg>

<div class="abs touch">
  <h4>Get in touch</h4>
  <dl>
    <dt>Address:</dt><dd>48 Harbor Lane, Coralview<br>Florida - 33120</dd>
    <dt>Telephone:</dt><dd>+1-877-VOSTIMO (867 8466)</dd>
    <dt>FAX:</dt><dd>+458-2190</dd>
    <dt>E-mail:</dt><dd><a href="#">mail@vostimo.net</a></dd>
  </dl>
</div>

<div class="abs footer">Copyright © 2014, vostimo.net, All rights reserved.</div>
</body>
</html>
```